Pathways to Brightmoor Land Ventures

size of the ad - 8”x 10.75" plus 0.25" bleed
I would like an ad for a magazine that will stand out and make people want to read the ad.
The ad should not be crowded and people reading the ad will be able to read the text.
I would like it to be a creative and modern-day design.
the list of topics should not be the focus of the ad.
the text is attached.
If you decide to use people in the ad then please no ladies.
please note that leave over 1 inch for the bottom of the footer

```html
<!DOCTYPE html>
<html lang="en">
<head>
<meta charset="UTF-8">
<title>Real Estate Course</title>
<link href="https://fonts.googleapis.com/css2?family=Poppins:wght@400;500;600;700;800&display=swap" rel="stylesheet">
<style>
  :root{
    --gold:#c98d2e;
    --gold-deep:#a86f1c;
    --band:#e3ae5d;
    --panel:#efcf8e;
    --cream:#fbf1d9;
    --cream-light:#fdf7e8;
    --ink:#2e2a26;
    --page-edge:#e9bd6c;
  }
  *{margin:0;padding:0;box-sizing:border-box}
  html,body{width:720px;height:1200px;overflow:hidden;background:var(--cream)}
  body{font-family:'Poppins',sans-serif;color:var(--ink)}
  .ad{
    position:relative;width:720px;height:1200px;overflow:hidden;
    background:
      radial-gradient(ellipse at 50% 0%, var(--page-edge) 0%, rgba(233,189,108,0) 55%),
      radial-gradient(ellipse at 20% 75%, rgba(255,255,255,.6) 0%, rgba(255,255,255,0) 40%),
      linear-gradient(180deg,#f3d394 0%,var(--cream) 40%,var(--cream-light) 70%,#f8e6bd 100%);
  }
  .ad-title{
    position:absolute;top:46px;left:0;width:100%;text-align:center;
    font-weight:800;font-size:60px;letter-spacing:-0.5px;color:var(--gold);line-height:1;
  }
  .hero-photo{
    position:absolute;top:130px;left:150px;width:420px;height:290px;
    background:radial-gradient(ellipse at 50% 55%, #d9c7a6 0%, #e8d3a6 35%, rgba(246,230,196,0) 70%);
  }
  .course-name{
    position:absolute;top:448px;left:0;width:100%;text-align:center;
    font-weight:700;font-size:26px;color:var(--gold);letter-spacing:.2px;
  }
  .tagline{
    position:absolute;top:492px;left:0;width:100%;text-align:center;
    font-weight:600;font-size:23px;line-height:1.55;color:var(--ink);
  }
  .details-frame{
    position:absolute;top:612px;left:-2px;width:338px;height:362px;
    border:1.5px solid var(--gold);border-left:none;border-radius:0 26px 26px 0;
  }
  .details-panel{
    position:absolute;top:630px;left:0;width:318px;height:326px;
    background:linear-gradient(180deg,#f2d79c,var(--panel));
    border-radius:0 22px 22px 0;padding:20px 0 0 38px;
  }
  .detail{margin-bottom:30px}
  .tag{
    position:relative;display:inline-block;background:var(--band);
    color:var(--gold-deep);font-weight:700;font-size:17px;letter-spacing:.5px;
    padding:1px 8px 0 0;line-height:1.35;box-shadow:2px 2px 3px rgba(150,100,30,.25);
  }
  .tag .clip{position:absolute;left:-14px;top:-7px}
  .detail p{font-size:16.5px;font-weight:500;line-height:1.3;margin-top:6px;color:var(--ink)}
  .topics-head{
    position:absolute;top:626px;left:350px;width:282px;height:58px;
    background:var(--band);padding:3px 0 0 30px;
    color:var(--gold-deep);font-weight:700;font-size:21px;line-height:1.25;letter-spacing:.5px;
    box-shadow:2px 3px 4px rgba(150,100,30,.25);
  }
  .topics-head .clip{position:absolute;left:6px;top:-8px}
  .topics{position:absolute;top:706px;left:378px;list-style:none}
  .topics li{display:flex;align-items:center;gap:9px;font-size:15.5px;font-weight:500;height:30px;color:var(--ink)}
</style>
</head>
<body>
<main class="ad">
  <h1 class="ad-title">REAL ESTATE COURSE</h1>

  <div class="hero-photo" role="img" aria-label="Photograph of a small businessman figure seated on a tall stack of coins beside a shorter stack, above soft clouds"></div>

  <h2 class="course-name">PATHWAYS TO BRIGHTMOOR LAND VENTURES</h2>
  <p class="tagline">INVESTING IN KNOWLEDGE IS INVESTING<br>IN OPPORTUNITIES.</p>

  <div class="details-frame"></div>
  <section class="details-panel">
    <div class="detail">
      <span class="tag"><svg class="clip" width="10" height="22" viewBox="0 0 10 22"><path d="M3 20V5a2 2 0 0 1 4 0v12" fill="none" stroke="#5a4a36" stroke-width="1.4"/></svg>LARKHAVEN</span>
      <p>10 -Tuesday evenings sessions</p>
    </div>
    <div class="detail">
      <span class="tag"><svg class="clip" width="10" height="22" viewBox="0 0 10 22"><path d="M3 20V5a2 2 0 0 1 4 0v12" fill="none" stroke="#5a4a36" stroke-width="1.4"/></svg>STARTING FEB.28</span>
      <p>Limited Partial Scholarships</p>
    </div>
    <div class="detail">
      <span class="tag"><svg class="clip" width="10" height="22" viewBox="0 0 10 22"><path d="M3 20V5a2 2 0 0 1 4 0v12" fill="none" stroke="#5a4a36" stroke-width="1.4"/></svg>EARLY BIRD SPECIAL</span>
      <p>For those that started or<br>would like to go into<br>real estate</p>
    </div>
  </section>

  <div class="topics-head">
    <svg class="clip" width="16" height="34" viewBox="0 0 16 34"><path d="M5 32V6a3.5 3.5 0 0 1 7 0v20" fill="none" stroke="#4a3d2e" stroke-width="1.8"/></svg>
    TOPICS:<br>PARTIAL LISTING
  </div>

  <ul class="topics">
    <li><svg width="12" height="11" viewBox="0 0 12 11"><path d="M6 1 1 5.5h1.5V10h7V5.5H11z" fill="none" stroke="#c98d2e" stroke-width="1.4"/></svg>Real estate investment strategies</li>
    <li><svg width="12" height="11" viewBox="0 0 12 11"><path d="M6 1 1 5.5h1.5V10h7V5.5H11z" fill="none" stroke="#c98d2e" stroke-width="1.4"/></svg>Due diligence</li>
    <li><svg width="12" height="11" viewBox="0 0 12 11"><path d="M6 1 1 5.5h1.5V10h7V5.5H11z" fill="none" stroke="#c98d2e" stroke-width="1.4"/></svg>Financing</li>
    <li><svg width="12" height="11" viewBox="0 0 12 11"><path d="M6 1 1 5.5h1.5V10h7V5.5H11z" fill="none" stroke="#c98d2e" stroke-width="1.4"/></svg>Underwriting</li>
    <li><svg width="12" height="11" viewBox="0 0 12 11"><path d="M6 1 1 5.5h1.5V10h7V5.5H11z" fill="none" stroke="#c98d2e" stroke-width="1.4"/></svg>Property management</li>
    <li><svg width="12" height="11" viewBox="0 0 12 11"><path d="M6 1 1 5.5h1.5V10h7V5.5H11z" fill="none" stroke="#c98d2e" stroke-width="1.4"/></svg>Real estate Legal basics</li>
    <li><svg width="12" height="11" viewBox="0 0 12 11"><path d="M6 1 1 5.5h1.5V10h7V5.5H11z" fill="none" stroke="#c98d2e" stroke-width="1.4"/></svg>Sourcing deals</li>
    <li><svg width="12" height="11" viewBox="0 0 12 11"><path d="M6 1 1 5.5h1.5V10h7V5.5H11z" fill="none" stroke="#c98d2e" stroke-width="1.4"/></svg>Syndication</li>
    <li><svg width="12" height="11" viewBox="0 0 12 11"><path d="M6 1 1 5.5h1.5V10h7V5.5H11z" fill="none" stroke="#c98d2e" stroke-width="1.4"/></svg>Dealing with brokers</li>
    <li><svg width="12" height="11" viewBox="0 0 12 11"><path d="M6 1 1 5.5h1.5V10h7V5.5H11z" fill="none" stroke="#c98d2e" stroke-width="1.4"/></svg>Tax fundamentals</li>
  </ul>
</main>
</body>
</html>
```